Wedding Photo Studio needs custom webpage

I'm changing up my service offering to offer multiple editing styles. I'm looking to update my website to reflect that but still showcase my dreamy edits as an attention grabbing part of the website.

I will have 4 color editing styles (Lucian's Hallmark, Bright & Airy, Velvet Umber, Dreamy) and one black and white style. I have attached sample images in each style.

I also attached a couple dreamy edits that can be used as attention grabbing images.

I'm hoping for some functionality that perhaps takes a single image and divides it by 4 to show 25% in each style that can be clicked on and would 'maximize' the carousel to that style but still have a functionality to go to a different style after being maximized.

You can see www.lucianvphotography-demo.com for the current design and content. It doesn't have to be too different (but can be). It just needs to showcase the multiple editing styles effectively.

Target Market(s)

Couples who are having $20-50k weddings.

Industry/Entity Type

Photography

Coding

Coded - Design and coding required

Number of Pages Required

3 page

Colors

Designer to choose colors to be used in the design.

Requirements
Must have
• Pricing page with toggles for (off-season/on-season, Saturday/non-saturday) accurate pricing, good way to show multiple editing style photos.

```html
<!DOCTYPE html>
<html lang="en">
<head>
<meta charset="utf-8">
<title>Lucian V Photography – Wedding Photographer Kitchener-Waterloo</title>
<link href="https://fonts.googleapis.com/css2?family=Montserrat:wght@400;500;600;700;800;900&family=Allura&display=swap" rel="stylesheet">
<style>
:root{
  --blue:#0a4fa6;
  --ink:#1b1b1b;
  --text:#4a4a4a;
  --white:#ffffff;
  --bar:#1e1e1e;
  --footer:#222222;
  --card-shadow:0 4px 18px rgba(0,0,0,.10);

  /* editing-style tone palettes */
  --bw-dark:#2b2b2b; --bw-mid:#7c7c7c; --bw-light:#e4e4e4;
  --airy-green:#9fbf7a; --airy-cream:#f4efe6; --airy-blush:#f1d9cf;
  --umber-deep:#4a2e1e; --umber-rust:#9a4a2a; --umber-gold:#c9955a;
  --dream-rose:#d9a7ad; --dream-peach:#f0c9a0; --dream-lilac:#b9a6c4;
  --night-navy:#121c36; --night-amber:#e0813c;
}
*{margin:0;padding:0;box-sizing:border-box}
html,body{width:1200px;height:4748px;overflow:hidden;background:var(--white)}
body{position:relative;font-family:'Montserrat',sans-serif;color:var(--ink)}
.abs{position:absolute}
.script{font-family:'Allura',cursive;color:var(--blue);font-weight:400}
.photo{position:absolute;overflow:hidden}

/* tone treatments per editing style */
.tone-bw{background:
  radial-gradient(ellipse 40% 55% at 55% 62%,var(--bw-light) 0%,rgba(228,228,228,0) 70%),
  radial-gradient(ellipse 30% 40% at 35% 45%,#1c1c1c 0%,rgba(28,28,28,0) 75%),
  linear-gradient(165deg,#3a3a3a 0%,var(--bw-mid) 45%,#b5b5b5 70%,#4b4b4b 100%)}
.tone-airy{background:
  radial-gradient(ellipse 45% 55% at 50% 70%,var(--airy-cream) 0%,rgba(244,239,230,0) 72%),
  radial-gradient(ellipse 35% 30% at 50% 35%,var(--airy-blush) 0%,rgba(241,217,207,0) 75%),
  linear-gradient(170deg,#6f8f48 0%,var(--airy-green) 40%,#dfe3cf 80%,#eeeae0 100%)}
.tone-umber{background:
  radial-gradient(ellipse 40% 55% at 48% 55%,#2e3550 0%,rgba(46,53,80,0) 75%),
  radial-gradient(ellipse 50% 40% at 85% 25%,var(--umber-gold) 0%,rgba(201,149,90,0) 75%),
  linear-gradient(165deg,var(--umber-deep) 0%,#6b5a3a 45%,var(--umber-rust) 100%)}
.tone-dreamy{background:
  radial-gradient(ellipse 45% 55% at 50% 60%,#f6eee6 0%,rgba(246,238,230,0) 72%),
  radial-gradient(ellipse 30% 25% at 70% 55%,var(--dream-rose) 0%,rgba(217,167,173,0) 75%),
  linear-gradient(165deg,#8a7560 0%,var(--dream-peach) 45%,#cdb8a8 100%)}

/* nav */
.nav{left:0;top:0;width:1200px;height:63px;background:var(--white);z-index:3}
.brand{position:absolute;left:83px;top:20px;display:flex;align-items:center;gap:8px;color:var(--blue);font-weight:600;font-size:15px;letter-spacing:.4px}
.brand-dot{width:10px;height:10px;border-radius:50%;background:var(--blue)}
.menu{position:absolute;left:409px;top:25px;display:flex;align-items:center;gap:20px;font-size:11px;letter-spacing:.6px;color:#333}
.menu .sep{width:5px;height:5px;border-radius:50%;background:var(--blue)}
.contact-btn{position:absolute;left:992px;top:15px;width:127px;height:33px;background:var(--blue);color:var(--white);border-radius:3px;font-size:10.5px;font-weight:700;display:flex;align-items:center;justify-content:center;gap:6px}

/* hero */
.hero-bg{left:0;top:63px;width:1200px;height:606px;background:
  radial-gradient(ellipse 30% 40% at 15% 20%,#bdbdbd 0%,rgba(189,189,189,0) 75%),
  radial-gradient(ellipse 30% 40% at 88% 25%,#c4c4c4 0%,rgba(196,196,196,0) 75%),
  linear-gradient(180deg,#d6d6d6 0%,#e6e6e6 50%,#f3f3f3 100%)}
.hero-script{left:0;width:1200px;top:112px;text-align:center;font-size:60px;line-height:1}
.hero-title{left:0;width:1200px;top:175px;text-align:center;font-size:53px;font-weight:800;letter-spacing:.5px;color:var(--ink)}
.arrow{width:30px;height:30px;border-radius:50%;background:var(--blue);display:flex;align-items:center;justify-content:center}
.hero-warm{background:
  radial-gradient(ellipse 35% 30% at 45% 45%,#3b2a22 0%,rgba(59,42,34,0) 75%),
  radial-gradient(ellipse 45% 40% at 50% 80%,#f1ede8 0%,rgba(241,237,232,0) 72%),
  radial-gradient(ellipse 40% 30% at 80% 30%,#b5402a 0%,rgba(181,64,42,0) 75%),
  linear-gradient(170deg,#7a4030 0%,#6a5a43 35%,#9a8c7c 65%,#dcd6ce 100%)}

/* about */
.section-title{left:0;width:1200px;text-align:center;font-weight:800;font-size:38px;letter-spacing:.5px;color:var(--ink)}
.about-copy{left:236px;top:853px;width:728px;text-align:center;font-size:10px;line-height:16px;color:var(--text)}
.about-photo{background:
  radial-gradient(ellipse 22% 40% at 20% 35%,#9a948a 0%,rgba(154,148,138,0) 75%),
  radial-gradient(ellipse 16% 45% at 57% 55%,#efe9e2 0%,rgba(239,233,226,0) 72%),
  radial-gradient(ellipse 14% 45% at 69% 55%,#1f2638 0%,rgba(31,38,56,0) 75%),
  radial-gradient(ellipse 25% 50% at 92% 30%,#c07a3a 0%,rgba(192,122,58,0) 75%),
  linear-gradient(110deg,#6e6a60 0%,#7d7260 40%,#5a5244 60%,#9a6a3a 100%)}
.cities{left:188px;top:1421px;width:826px;height:48px;background:var(--bar);display:flex;align-items:center;justify-content:space-between;padding:0 36px;color:var(--white);font-size:10.5px;font-weight:600}
.cities .sep{width:4px;height:4px;border-radius:50%;background:var(--blue)}

/* styles */
.style-label{color:var(--white);font-weight:800;font-size:19px;letter-spacing:.5px}
.style-tab{left:804px;top:1701px;width:184px;height:33px;background:var(--ink);color:var(--white);font-weight:800;font-size:13px;display:flex;align-items:center;justify-content:center}
.dots{left:844px;top:2221px;display:flex;gap:10px}
.dots span{width:6px;height:6px;border-radius:50%;background:rgba(255,255,255,.75)}
.dots span.on{background:var(--blue)}

/* testimonials */
.card{position:absolute;background:var(--white);box-shadow:var(--card-shadow);padding:32px 28px 0 28px}
.card-head{display:flex;align-items:center;gap:14px;margin-bottom:18px}
.avatar{width:34px;height:34px;border-radius:50%;background:linear-gradient(135deg,#c9a58a,#7d5a48)}
.card-name{color:var(--blue);font-weight:700;font-size:11.5px}
.card-body{font-size:9.6px;line-height:15.5px;color:var(--text)}
.quote{margin-top:20px;color:var(--blue);font-size:40px;font-weight:900;line-height:.6;font-family:Georgia,serif}

/* dreamy */
.dreamy-sunset{background:
  radial-gradient(ellipse 40% 30% at 30% 20%,#f6d3b0 0%,rgba(246,211,176,0) 75%),
  radial-gradient(ellipse 20% 45% at 60% 55%,#f4ede6 0%,rgba(244,237,230,0) 72%),
  radial-gradient(ellipse 18% 40% at 45% 50%,#8f8a86 0%,rgba(143,138,134,0) 75%),
  linear-gradient(175deg,var(--dream-lilac) 0%,var(--dream-rose) 25%,var(--dream-peach) 45%,#a9a3a0 70%,#d8d2cc 100%)}
.dreamy-night{background:
  radial-gradient(ellipse 50% 25% at 70% 30%,#f2a15a 0%,rgba(242,161,90,0) 75%),
  radial-gradient(ellipse 15% 30% at 55% 78%,#f3ece6 0%,rgba(243,236,230,0) 72%),
  radial-gradient(ellipse 60% 25% at 50% 92%,#b07a50 0%,rgba(176,122,80,0) 75%),
  linear-gradient(175deg,var(--night-navy) 0%,#1f2948 25%,#6a3a48 50%,var(--night-amber) 65%,#5a3a2a 100%)}
.dreamy-box{left:475px;top:3432px;width:249px;height:140px;background:#0c0c0c;border-radius:10px;text-align:center;color:var(--white)}
.dreamy-box .script{color:var(--blue);font-size:36px;display:block;margin-top:22px;line-height:1}
.dreamy-box .word{font-size:34px;letter-spacing:2px;font-weight:500;display:block;margin-top:6px}

/* blogs */
.blog-hall{background:
  radial-gradient(ellipse 12% 60% at 20% 40%,#e08a3a 0%,rgba(224,138,58,0) 75%),
  radial-gradient(ellipse 12% 60% at 80% 40%,#e08a3a 0%,rgba(224,138,58,0) 75%),
  radial-gradient(ellipse 10% 30% at 50% 70%,#d8d4cf 0%,rgba(216,212,207,0) 72%),
  linear-gradient(180deg,#1e120a 0%,#6a3a18 45%,#2a1a10 100%)}
.blog-glass{background:
  radial-gradient(ellipse 40% 40% at 50% 30%,#8fb4d4 0%,rgba(143,180,212,0) 75%),
  radial-gradient(ellipse 50% 25% at 50% 80%,#6a5a4a 0%,rgba(106,90,74,0) 75%),
  linear-gradient(180deg,#3a5a7a 0%,#2a3a4a 55%,#4a4038 100%)}
.post{position:absolute;width:402px}
.post-date{color:var(--blue);font-weight:700;font-size:9.5px}
.post-title{margin-top:8px;width:320px;font-size:20px;line-height:24px;font-weight:500;color:var(--ink);letter-spacing:.3px}
.post-sub{margin-top:8px;font-size:11.5px;font-weight:700}
.post-copy{margin-top:16px;font-size:9.5px;line-height:15.5px;color:var(--text)}
.post-more{margin-top:20px;font-size:9.5px;font-weight:700;color:var(--blue);text-decoration:underline}

/* footer */
.footer{left:0;top:4543px;width:1200px;height:205px;background:var(--footer)}
.social{width:44px;height:44px;border-radius:50%}
.copyright{left:0;width:1200px;text-align:center;color:var(--white);font-size:12px}
</style>
</head>
<body>

<header class="abs nav">
  <div class="brand"><span>Lucian V Photography</span><span class="brand-dot"></span></div>
  <nav class="menu">
    <span>HOME</span><span class="sep"></span>
    <span>THE TEAM</span><span class="sep"></span>
    <span>PORTFOLIO</span><span class="sep"></span>
    <span>BLOG</span><span class="sep"></span>
    <span>PRICING</span>
  </nav>
  <div class="contact-btn">
    <svg width="10" height="10" viewBox="0 0 24 24"><path fill="#fff" d="M6.6 10.8a15.1 15.1 0 0 0 6.6 6.6l2.2-2.2c.3-.3.7-.4 1-.2 1.1.4 2.3.6 3.6.6.6 0 1 .4 1 1V20c0 .6-.4 1-1 1A17 17 0 0 1 3 4c0-.6.4-1 1-1h3.5c.6 0 1 .4 1 1 0 1.3.2 2.5.6 3.6.1.3 0 .7-.2 1z"/></svg>
    Contact Me
  </div>
</header>

<section class="hero">
  <div class="abs hero-bg" role="img" aria-label="Faded black and white photo of a wedding venue courtyard"></div>
  <div class="abs hero-script script">Wedding Photographer</div>
  <h1 class="abs hero-title">KITCHENER-WATERLOO</h1>
  <div class="abs arrow" style="left:42px;top:350px"><svg width="10" height="10" viewBox="0 0 10 10"><path d="M7 1 2 5l5 4z" fill="#fff"/></svg></div>
  <div class="abs arrow" style="left:1126px;top:350px"><svg width="10" height="10" viewBox="0 0 10 10"><path d="M3 1l5 4-5 4z" fill="#fff"/></svg></div>
  <div class="photo hero-warm" style="left:188px;top:280px;width:262px;height:485px" role="img" aria-label="Couple on stone steps before an ivy-covered doorway in autumn colour, signature edit"></div>
  <div class="photo tone-bw" style="left:470px;top:280px;width:262px;height:371px" role="img" aria-label="Black and white edit of the couple at the doorway steps"></div>
  <div class="photo hero-warm" style="left:756px;top:280px;width:254px;height:479px" role="img" aria-label="Couple at an ivy-covered doorway, warm umber edit"></div>
</section>

<section class="about">
  <h2 class="abs section-title" style="top:790px">ABOUT ME</h2>
  <p class="abs about-copy">I am an accountant by day, photographer by night. I once read a happy life is had by loving your job, loving your creative hobby and the love of family; photography is one part of that for me. I focus primarily on wedding photography in southern Ontario. I cover Toronto, Hamilton, Kitchener, Waterloo, London and anywhere in the world you want to send me. If you like what I do, please reach out; I'm happy to meet with you and chat more about your big day.</p>
  <div class="abs script" style="left:0;width:1200px;top:930px;text-align:center;font-size:40px">Lucian Varela</div>
  <div class="photo about-photo" style="left:188px;top:1004px;width:826px;height:417px" role="img" aria-label="Bride and groom embracing beside a carved stone balustrade in autumn"></div>
  <div class="abs cities">
    <span>Toronto</span><span class="sep"></span><span>Hamilton</span><span class="sep"></span><span>London</span><span class="sep"></span><span>Niagara</span><span class="sep"></span><span>Cambridge</span><span class="sep"></span><span>Mississauga</span><span class="sep"></span><span>Brampton</span><span class="sep"></span><span>Guelph</span><span class="sep"></span><span>Burlington</span>
  </div>
</section>

<section class="styles">
  <div class="abs script" style="left:0;width:1200px;top:1545px;text-align:center;font-size:52px">Lucian Varela's</div>
  <h2 class="abs section-title" style="top:1600px">EDITING STYLES</h2>
  <div class="photo tone-bw" style="left:18px;top:1683px;width:277px;height:276px" role="img" aria-label="Groom's jacket and boutonniere, black and white edit"></div>
  <div class="abs style-label" style="left:18px;top:1808px;width:277px;text-align:center">BLACK &amp; WHITE</div>
  <div class="photo tone-airy" style="left:313px;top:1683px;width:277px;height:276px" role="img" aria-label="Bride by a garden waterfall, bright and airy edit"></div>
  <div class="photo tone-umber" style="left:18px;top:1978px;width:277px;height:276px" role="img" aria-label="Groom in a navy suit among autumn leaves, velvet umber edit"></div>
  <div class="photo tone-dreamy" style="left:313px;top:1978px;width:277px;height:276px" role="img" aria-label="Bride's gown and bouquet, dreamy edit"></div>
  <div class="photo tone-bw" style="left:608px;top:1683px;width:573px;height:571px" role="img" aria-label="Black and white edit of the couple walking hand in hand along a garden path"></div>
  <div class="abs style-tab">BLACK &amp; WHITE</div>
  <div class="abs dots"><span class="on"></span><span></span><span></span><span></span><span></span><span></span></div>
</section>

<section class="testimonials">
  <h2 class="abs section-title" style="top:2338px">TESTIMONIALS</h2>

  <article class="card" style="left:188px;top:2422px;width:262px;height:383px">
    <div class="card-head"><div class="avatar"></div><div class="card-name">Noah &amp; Elise</div></div>
    <p class="card-body">We got married September 30 and hired Lucian and we are VERY HAPPY we did! Lucian did an AMAZING job!! He is very professional, very organized, got the most beautiful shots, he captured the all the most important moments in such beautiful ways, we were speechless when we saw the amazing photos from our wedding. Would very much recommend to anyone looking for a photographer and his prices are very reasonable. Thank you so much again Lucian!</p>
    <div class="quote">”</div>
  </article>
  <article class="card" style="left:188px;top:2824px;width:262px;height:289px">
    <div class="card-head"><div class="avatar"></div><div class="card-name">Owen &amp; Clara</div></div>
    <p class="card-body">Lucian did a fabulous job on both our engagement and wedding photos. We were very impressed with not only the posed shots but also all of the candid ones. He was very professional, organized and accommodating. We have already recommended him to numerous people and will continue to do so!</p>
    <div class="quote">”</div>
  </article>

  <article class="card" style="left:470px;top:2422px;width:262px;height:287px">
    <div class="card-head"><div class="avatar"></div><div class="card-name">Marco &amp; Jenna</div></div>
    <p class="card-body">Lucian did an outstanding job on our wedding photos! We got so so much more for so so much less. Thanks again Lucian, you exceeded our expectations and then some. I recommend him 100 times over!</p>
    <div class="quote">”</div>
  </article>
  <article class="card" style="left:470px;top:2728px;width:262px;height:385px">
    <div class="card-head"><div class="avatar"></div><div class="card-name">Reid &amp; Sofia</div></div>
    <p class="card-body">Lucian did an absolutely amazing job shooting our wedding! He was attentive, organized and he made sure we got all our "must-have" shots. His eye for beautiful shots was great and his photography was very creative! All of our family and our guests were raving about about great he was and we couldn't agree more! Thank you for capturing our special day and giving us perfect memories to last a lifetime!</p>
    <div class="quote">”</div>
  </article>

  <article class="card" style="left:748px;top:2422px;width:262px;height:383px">
    <div class="card-head"><div class="avatar"></div><div class="card-name">Theo &amp; Amara</div></div>
    <p class="card-body">Lucian is the absolute best! He did a SPECTACULAR job with our wedding photos. He got images of everything, even the things that we never thought he would notice. Hands down Lucian is the best photographer I have seen in the area and you will not be disappointed.</p>
    <div class="quote">”</div>
  </article>
  <article class="card" style="left:748px;top:2824px;width:262px;height:289px">
    <div class="card-head"><div class="avatar"></div><div class="card-name">Julian &amp; Rosa</div></div>
    <p class="card-body">We would just love to thank Lucian for his amazing work for our wedding! He was able to capture those moments that showed our personality the most! We really had no suggestions to give him because we didn't prepare for this part... but he managed to capture the "theme" of the wedding! He even stayed longer than expected!! Thank you Lucian!!!</p>
    <div class="quote">”</div>
  </article>
</section>

<section class="dreamy">
  <div class="photo dreamy-sunset" style="left:13px;top:3201px;width:580px;height:599px" role="img" aria-label="Couple kissing by a riverside railing at sunset, dreamy edit"></div>
  <div class="photo dreamy-night" style="left:606px;top:3201px;width:581px;height:599px" role="img" aria-label="Couple dancing under a lit venue canopy at night with a starry sky, dreamy edit"></div>
  <div class="abs dreamy-box"><span class="script">Lucian Varela</span><span class="word">DREAMY</span></div>
</section>

<section class="blogs">
  <h2 class="abs section-title" style="top:3885px">LATEST BLOGS</h2>
  <div class="photo blog-hall" style="left:188px;top:3968px;width:402px;height:227px" role="img" aria-label="Couple beneath illuminated stone columns at night"></div>
  <div class="photo blog-glass" style="left:610px;top:3968px;width:402px;height:227px" role="img" aria-label="Ceremony inside a glass-walled waterfront hall"></div>

  <article class="post" style="left:188px;top:4232px">
    <div class="post-date">May 2, 2018</div>
    <h3 class="post-title">EVAN &amp; MIRA AT THE CEDAR HALL ESTATE</h3>
    <div class="post-sub">Toronto Wedding Photographer</div>
    <p class="post-copy">Evan &amp; Mira's wedding at the newish Cedar Hall Estate in Scarborough was quite possibly the wildest wedding party I have ever been to – they had a dancing robot! Now, it's ridiculously hard to describe what this entails, so just make sure you don't gloss over the party shots at the end because it is absolutely awesome.</p>
    <div class="post-more">Read more</div>
  </article>
  <article class="post" style="left:610px;top:4232px">
    <div class="post-date">September 6, 2017</div>
    <h3 class="post-title">HANNAH &amp; COLE AT HARBOURVIEW PAVILION</h3>
    <div class="post-sub">Burlington Wedding Photographer</div>
    <p class="post-copy">I was looking forward to Hannah &amp; Cole's special day since they booked me as it was going to be my first time shooting at Harbourview Pavilion, a venue which I had on my bucket list for the last few years. It's waterfront location, with complete glass surroundings, and the most amazing architecture has made me long to photograph a wedding...</p>
    <div class="post-more">Read more</div>
  </article>
</section>

<footer class="abs footer">
  <div class="abs social" style="left:544px;top:61px;background:var(--blue)" role="img" aria-label="Social profile link"></div>
  <div class="abs social" style="left:612px;top:61px;background:#c23a7a" role="img" aria-label="Social profile link"></div>
  <p class="abs copyright" style="top:128px">Copyright 2025 <b>Lucian Varela Photography.</b></p>
</footer>

</body>
</html>
```